Out of town New Masters of Accounting

size of ad is 7” x 9.6”
please leave one inch on bottom for footer
We want to attract out of town students to join this master's in accounting program.
You DO NOT  have to use a picture of a person.
But if you do, it should be a  male with a white shirt and should not have long hair.(look like a young executive)
THE TEXT OF THE AD IS IN THE ATTACHMENTS
THE CAP LETTERS ARE THE INSTRUCTIONS

The age we are trying to attract is from 20-30 of ages.
- a clear ad .. the text should not take up the entire ad.. it should not be very crowded -
it should be an attractive ad that people would want to see and stand out
- the text very big and take up the entire ad

```html
<!DOCTYPE html>
<html lang="en">
<head>
<meta charset="utf-8">
<title>Master's of Science in Accounting – Remote Program</title>
<link href="https://fonts.googleapis.com/css2?family=Poppins:wght@500;600;700;800&display=swap" rel="stylesheet">
<style>
  :root {
    --sky: #1fa8ea;
    --sky-light: #34b3ec;
    --navy: #1b3d86;
    --band-deep: #0f5aa8;
    --band-mid: #1a73c4;
    --sun: #f7c51e;
    --ink: #1d1d1f;
    --white: #ffffff;
    --footer-black: #0b0b0c;
    --photo-dark: #1c1f24;
    --photo-mid: #4a5058;
    --photo-light: #8a9098;
    --badge: #f0a33a;
  }
  * { box-sizing: border-box; margin: 0; padding: 0; }
  html, body { width: 875px; height: 1200px; overflow: hidden; background: var(--white); }
  body { font-family: 'Poppins', sans-serif; }

  .ad { position: relative; width: 875px; height: 1200px; overflow: hidden; background: var(--white); }

  .hero-photo {
    position: absolute; left: 0; top: 0; width: 875px; height: 600px;
    background: radial-gradient(ellipse at 70% 30%, var(--photo-light) 0%, var(--photo-mid) 40%, var(--photo-dark) 100%);
  }

  .hero-text { position: absolute; left: 0; top: 0; width: 875px; height: 520px; text-align: center; color: var(--white); }
  .hero-lead { position: absolute; top: 78px; width: 100%; font-size: 27px; font-weight: 700; }
  .hero-title {
    position: absolute; top: 126px; width: 100%;
    font-size: 86px; font-weight: 800; line-height: 84px; color: var(--sky);
    letter-spacing: 1px; text-transform: uppercase;
  }
  .hero-since { position: absolute; top: 392px; width: 100%; font-size: 25px; font-weight: 700; }
  .hero-duration { position: absolute; top: 442px; width: 100%; font-size: 30px; font-weight: 700; color: var(--sun); }
  .swoosh { position: absolute; left: 360px; top: 490px; }

  .program-band { position: absolute; left: 0; top: 555px; }
  .band-new {
    position: absolute; left: 28px; top: 600px;
    font-size: 66px; font-weight: 800; color: var(--sun); line-height: 1; letter-spacing: -1px;
  }
  .band-remote {
    position: absolute; left: 212px; top: 603px;
    font-size: 27px; font-weight: 700; color: var(--white); line-height: 33px; text-transform: uppercase;
  }
  .start-box { position: absolute; left: 592px; top: 572px; width: 280px; text-align: center; text-transform: uppercase; }
  .start-label { font-size: 23px; font-weight: 700; color: var(--white); line-height: 28px; }
  .start-date { font-size: 44px; font-weight: 800; color: var(--white); line-height: 50px; }
  .start-price { font-size: 22px; font-weight: 800; color: var(--navy); line-height: 30px; }

  .placement { position: absolute; left: 68px; top: 757px; }
  .placement-heading { font-size: 25px; font-weight: 600; color: var(--sky); margin-bottom: 12px; }
  .placement-list { list-style: none; }
  .placement-list li {
    display: flex; align-items: center; gap: 14px;
    font-size: 26px; font-weight: 500; color: var(--ink); height: 49px;
  }

  .partner-box {
    position: absolute; left: 70px; top: 956px; width: 486px; height: 94px;
    border: 2px solid var(--navy); border-radius: 22px;
    box-shadow: 0 5px 6px rgba(0,0,0,0.18);
    text-align: center; padding-top: 16px; color: var(--ink);
  }
  .partner-name { font-size: 21px; font-weight: 500; line-height: 28px; }
  .partner-program { font-size: 21px; font-weight: 700; line-height: 28px; }

  .ranking-badge { position: absolute; left: 622px; top: 790px; }

  .footer { position: absolute; left: 0; top: 1072px; width: 875px; height: 128px; }
  .footer-bg { position: absolute; left: 0; top: 0; }
  .org-name {
    position: absolute; left: 22px; top: 20px; width: 330px;
    display: flex; align-items: center; gap: 10px;
    font-size: 22px; font-weight: 700; color: var(--white); line-height: 26px;
  }
  .org-mark { width: 16px; height: 16px; background: var(--white); flex: none; }
  .org-parent {
    position: absolute; left: 0; top: 86px; width: 375px; height: 28px;
    font-size: 15px; font-weight: 700; color: var(--white); background: var(--navy);
    padding-left: 22px; line-height: 28px; text-transform: uppercase; letter-spacing: 0.3px;
  }
  .contact { position: absolute; left: 388px; top: 28px; color: var(--white); font-size: 14px; font-weight: 600; font-style: normal; }
  .contact-row { display: flex; align-items: center; gap: 8px; height: 31px; white-space: nowrap; }
  .contact-row svg { flex: none; }
  .audience {
    position: absolute; left: 752px; top: 10px; width: 110px; height: 102px;
    background: var(--sky); border-radius: 6px;
    display: flex; align-items: center; justify-content: center; text-align: center;
    font-size: 23px; font-weight: 800; color: var(--navy); line-height: 28px; text-transform: uppercase;
  }
</style>
</head>
<body>
<main class="ad">

  <div class="hero-photo" role="img" aria-label="Photo of a young executive in a white shirt drawing on a glass board with a financial line chart"></div>

  <header class="hero-text">
    <p class="hero-lead">Advance your career with a</p>
    <h1 class="hero-title">Master’s of<br>Science in<br>Accounting</h1>
    <p class="hero-since">Since 2005</p>
    <p class="hero-duration">Master’s in only 15 months</p>
  </header>
  <svg class="swoosh" width="400" height="45" viewBox="0 0 400 45" aria-hidden="true">
    <path d="M0 40 C 60 8, 180 -2, 400 10 C 200 8, 90 18, 14 44 Z" fill="var(--sun)"/>
  </svg>

  <svg class="program-band" width="875" height="180" viewBox="0 0 875 180" aria-hidden="true">
    <defs>
      <linearGradient id="bandFill" x1="0" y1="0" x2="1" y2="0">
        <stop offset="0" stop-color="var(--band-mid)"/>
        <stop offset="1" stop-color="var(--band-deep)"/>
      </linearGradient>
    </defs>
    <path d="M0 20 H560 Q600 20 615 50 L655 170 H0 Z" fill="url(#bandFill)"/>
    <path d="M610 8 H860 Q875 8 875 22 V120 Q875 130 862 130 H590 Q575 130 578 118 L590 22 Q593 8 610 8 Z" fill="var(--sky-light)"/>
  </svg>
  <div class="band-new">NEW!</div>
  <div class="band-remote">Remote program<br>for out of town<br>students</div>
  <div class="start-box">
    <div class="start-label">Beginning</div>
    <div class="start-date">August 17</div>
    <div class="start-price">New lower prices</div>
  </div>

  <section class="placement">
    <h2 class="placement-heading">BCN Job Placement Advantage</h2>
    <ul class="placement-list">
      <li><svg width="24" height="24" viewBox="0 0 24 24" aria-hidden="true"><circle cx="12" cy="12" r="10" fill="none" stroke="var(--sky)" stroke-width="3"/><path d="M7 12 l4 4 l6 -7" fill="none" stroke="var(--sky)" stroke-width="3" stroke-linecap="round"/></svg>96% Placement Rate</li>
      <li><svg width="24" height="24" viewBox="0 0 24 24" aria-hidden="true"><circle cx="12" cy="12" r="10" fill="none" stroke="var(--sky)" stroke-width="3"/><path d="M7 12 l4 4 l6 -7" fill="none" stroke="var(--sky)" stroke-width="3" stroke-linecap="round"/></svg>8 Placement Coordinators</li>
      <li><svg width="24" height="24" viewBox="0 0 24 24" aria-hidden="true"><circle cx="12" cy="12" r="10" fill="none" stroke="var(--sky)" stroke-width="3"/><path d="M7 12 l4 4 l6 -7" fill="none" stroke="var(--sky)" stroke-width="3" stroke-linecap="round"/></svg>Relationships with 100’s of Firms</li>
    </ul>
  </section>

  <div class="partner-box">
    <p class="partner-name">Harrow Crest University (HCU)</p>
    <p class="partner-program">Master’s in Accounting Program</p>
  </div>

  <svg class="ranking-badge" width="170" height="170" viewBox="0 0 170 170" role="img" aria-label="Program ranking badge">
    <circle cx="85" cy="85" r="80" fill="var(--badge)"/>
  </svg>

  <footer class="footer">
    <svg class="footer-bg" width="875" height="128" viewBox="0 0 875 128" aria-hidden="true">
      <rect x="360" y="18" width="515" height="110" fill="var(--footer-black)"/>
      <path d="M0 0 H300 Q350 0 362 20 L375 128 H0 Z" fill="var(--sky)"/>
    </svg>
    <div class="org-name"><span class="org-mark"></span>Brightline Career Network</div>
    <div class="org-parent">A non-profit of Civic Learning Alliance</div>
    <address class="contact">
      <div class="contact-row">
        <svg width="16" height="18" viewBox="0 0 16 18" aria-hidden="true"><path d="M8 1 C4 1 2 4 2 7 C2 11 8 17 8 17 C8 17 14 11 14 7 C14 4 12 1 8 1 Z" fill="none" stroke="var(--sky)" stroke-width="2"/><circle cx="8" cy="7" r="2" fill="var(--sky)"/></svg>
        Eastbrook, Millford, Lakeview Main Branch
      </div>
      <div class="contact-row">
        <svg width="16" height="16" viewBox="0 0 16 16" aria-hidden="true"><circle cx="8" cy="8" r="7" fill="none" stroke="var(--sky)" stroke-width="1.6"/><path d="M1 8 H15 M8 1 C4 5 4 11 8 15 M8 1 C12 5 12 11 8 15" fill="none" stroke="var(--sky)" stroke-width="1.4"/></svg>
        www.brightlinecn.org
        <svg width="16" height="16" viewBox="0 0 16 16" aria-hidden="true"><path d="M3 1 L6 1 L7 5 L5 6 C6 8 8 10 10 11 L11 9 L15 10 L15 13 C15 14 14 15 13 15 C7 14 2 9 1 3 C1 2 2 1 3 1 Z" fill="var(--sky)"/></svg>
        555 210 4400 x 120
      </div>
      <div class="contact-row">
        <svg width="18" height="14" viewBox="0 0 18 14" aria-hidden="true"><rect x="1" y="1" width="16" height="12" fill="none" stroke="var(--sky)" stroke-width="1.8"/><path d="M1 1 L9 8 L17 1" fill="none" stroke="var(--sky)" stroke-width="1.8"/></svg>
        admissions@brightlinecn.org
      </div>
    </address>
    <div class="audience">Men &amp;<br>Woman</div>
  </footer>

</main>
</body>
</html>
```